Notary Signing Agent Need Business card Design

Need a Business card design for my new company. RT Velo-Brisk LLC
Mobile Notary Signing Agent. I go to the customer for closing of Mortgage's Documents . possible signs of honesty, integrity and confidentiality.

Work with Title company to Notary Mortgage closing.

My Target Market is Title companies. Banks and Financial Institution.

Color Blue to Black Professional ) if needed some Green Little Red

And possible a company logo.

Mobile ( travel to clients ) Integrity, Honest Trustworthy. A show of Professional services.

Would like company name and my name on card

Use both sides and front with business name and my name. phone numbers.

Target Market(s)

Title company, Banks mortgage company

Industry/Entity Type

Travel

Contact Information for Business Card

Notary, Certified signing agent, Mobile

Colors
0455a3

Requirements
Must have
• Name of company , owners name phone number,
Nice to have
• blue and black color like a professional look but not limit to these only.
• a stand out from other cards .

```html
<!DOCTYPE html>
<html lang="en">
<head>
<meta charset="utf-8">
<title>RT Velo-Brisk LLC — Business Card Print Sheet</title>
<link rel="stylesheet" href="https://fonts.googleapis.com/css2?family=Saira:wght@500;600&display=swap">
<style>
  :root {
    --sheet: #000000;
    --crop-mark: #e6e6e6;
    --card-top: #445d7c;
    --card-mid: #eceef2;
    --card-bottom: #3f5445;
    --brand-ink: #0e3f5c;
    --text-ink: #1c1f22;
    --rule: #4a4d52;
  }
  html, body {
    margin: 0;
    padding: 0;
    width: 858px;
    height: 1200px;
    overflow: hidden;
    background: var(--sheet);
  }
  .print-sheet {
    position: relative;
    width: 858px;
    height: 1200px;
    background: var(--sheet);
    font-family: "Saira", sans-serif;
  }
  .crop-marks {
    position: absolute;
    inset: 0;
  }
  .card {
    position: absolute;
    left: 91px;
    width: 699px;
    height: 402px;
    background: linear-gradient(180deg,
      var(--card-top) 0%,
      #8894a8 28%,
      var(--card-mid) 56%,
      #a9afa8 70%,
      var(--card-bottom) 100%);
    overflow: hidden;
  }
  .card--front { top: 93px; }
  .card--back { top: 704px; }
  .brand-name {
    position: absolute;
    left: 0;
    right: 0;
    text-align: center;
    margin: 0;
    font-weight: 600;
    font-size: 52px;
    letter-spacing: 1px;
    color: var(--brand-ink);
    line-height: 1;
  }
  .card--front .brand-name { top: 180px; }
  .card--back .brand-name { top: 124px; }
  .contact {
    position: absolute;
    left: 0;
    right: 0;
    top: 196px;
    text-align: center;
    color: var(--text-ink);
  }
  .contact__name {
    display: inline-block;
    margin: 0;
    padding: 0 10px 1px;
    font-weight: 500;
    font-size: 24px;
    line-height: 1.1;
    border-bottom: 1px solid var(--rule);
  }
  .contact__title {
    margin: 3px 0 0;
    font-weight: 500;
    font-size: 13px;
  }
  .contact__phones {
    margin: 16px 0 0;
    font-weight: 500;
    font-size: 19px;
    letter-spacing: 2px;
    line-height: 1.1;
  }
</style>
</head>
<body>
<main class="print-sheet">
  <svg class="crop-marks" width="858" height="1200" viewBox="0 0 858 1200" aria-hidden="true">
    <g stroke="var(--crop-mark)" stroke-width="1.5">
      <!-- front card marks -->
      <line x1="91" y1="0" x2="91" y2="74"/>
      <line x1="790" y1="0" x2="790" y2="74"/>
      <line x1="0" y1="93" x2="74" y2="93"/>
      <line x1="808" y1="93" x2="858" y2="93"/>
      <line x1="0" y1="495" x2="74" y2="495"/>
      <line x1="808" y1="495" x2="858" y2="495"/>
      <line x1="91" y1="513" x2="91" y2="588"/>
      <line x1="790" y1="513" x2="790" y2="588"/>
      <!-- back card marks -->
      <line x1="91" y1="612" x2="91" y2="686"/>
      <line x1="790" y1="612" x2="790" y2="686"/>
      <line x1="0" y1="704" x2="74" y2="704"/>
      <line x1="808" y1="704" x2="858" y2="704"/>
      <line x1="0" y1="1108" x2="74" y2="1108"/>
      <line x1="808" y1="1108" x2="858" y2="1108"/>
      <line x1="91" y1="1125" x2="91" y2="1200"/>
      <line x1="790" y1="1125" x2="790" y2="1200"/>
    </g>
  </svg>

  <section class="card card--front" aria-label="Card front">
    <p class="brand-name">RT Velo-Brisk LLC</p>
  </section>

  <section class="card card--back" aria-label="Card back">
    <p class="brand-name">RT Velo-Brisk LLC</p>
    <div class="contact">
      <p class="contact__name">Daniel R. Hollis</p>
      <p class="contact__title">Notary &amp; Certified Signing Agent</p>
      <p class="contact__phones">850-555-0142<br>860-555-0176</p>
    </div>
  </section>
</main>
</body>
</html>
```